Brent's Business Cards

My husband is a self employed Cabinet Maker... who contracts to Building companies and clients directly.
He installs kitchesn, designs and also completes renovations and building work.

I would like a small, FUNKY, simple but eye catching design.

It needs to incorporate the following.
Custom Cabinets / Installations / Renovations / Design

Commercial and Residential

He does not have a Website or Facebook,
contact number is 0438 207 964 and email is brentkelway@mailpost.example

I would like a Grey/Silver on black, or blue covering.. I am open to colour designs?

Thank you. :-)

Target Market(s)

Building Companies
Clients
Other Trades people onsite,. to give out at job sites

Industry/Entity Type

Business

Contact Information for Business Card

Phone: 0438 207 964
Email: brentkelway@mailpost.example

Font styles to use
Sans Serif

Colors
0592cd
747474
474747
1b1b1b
85cae6

Requirements
Must have
• Funky, simple, eye catching design
• Would like use of Silver/Grey - and a colour that would complement this.
• Am open to ideas :-)
Nice to have
• We do not have a logo or picture, will leave this up to you if you think an image would be beneficial???
• Thank you.

Files

```html
<!DOCTYPE html>
<html lang="en">
<head>
<meta charset="UTF-8">
<title>Brent's Business Card</title>
<link rel="stylesheet" href="https://fonts.googleapis.com/css2?family=Exo+2:wght@400;500;600&display=swap">
<style>
  :root {
    --backdrop: #2a2a2a;
    --card-black: #1b1b1b;
    --card-edge: #474747;
    --text-white: #f4f4f4;
    --silver-light: #f2f2f2;
    --silver-mid: #b9b9b9;
    --silver-dark: #747474;
  }
  * { margin: 0; padding: 0; box-sizing: border-box; }
  html, body {
    width: 1200px;
    height: 1000px;
    overflow: hidden;
    background: var(--backdrop);
  }
  .canvas {
    width: 1200px;
    height: 1000px;
    display: flex;
    align-items: center;
    justify-content: center;
  }
  .business-card {
    position: relative;
    width: 1000px;
    height: 572px;
    background: var(--card-black);
    border: 1px solid var(--card-edge);
    font-family: "Exo 2", "Segoe UI", sans-serif;
    color: var(--text-white);
    text-align: center;
  }
  .owner-name {
    position: absolute;
    top: 118px;
    left: 0;
    right: 0;
    font-size: 60px;
    font-weight: 500;
    letter-spacing: 4px;
    background: linear-gradient(180deg, var(--silver-light) 0%, var(--silver-mid) 55%, var(--silver-dark) 100%);
    -webkit-background-clip: text;
    background-clip: text;
    color: transparent;
  }
  .services {
    position: absolute;
    top: 214px;
    left: 0;
    right: 0;
    font-size: 27px;
    font-weight: 400;
    letter-spacing: 0.5px;
    line-height: 1.6;
  }
  .contact-row {
    position: absolute;
    top: 420px;
    left: 0;
    right: 0;
    display: flex;
    align-items: center;
    justify-content: center;
    gap: 40px;
    font-size: 30px;
    font-weight: 500;
    letter-spacing: 0.5px;
  }
  .contact-divider {
    width: 2px;
    height: 52px;
    background: var(--text-white);
    transform: skewX(-14deg);
  }
</style>
</head>
<body>
  <main class="canvas">
    <section class="business-card">
      <h1 class="owner-name">BRENT KELWAY</h1>
      <p class="services">
        Custom Cabinets / Installations / Renovations / Design<br>
        Commercial and Residential
      </p>
      <div class="contact-row">
        <span class="contact-phone">0438 207 964</span>
        <span class="contact-divider" aria-hidden="true"></span>
        <span class="contact-email">brentkelway@mailpost.example</span>
      </div>
    </section>
  </main>
</body>
</html>
```